Talvor Visit cards serious but not sad

Hello, I'd like to design my visit cards with the logo Talvor (attached) the following information: Name: Karim Belmadi Title: Mobile Director: 33 (0) 6 72 18 35 09 Phone: 33 (0) 4 58 61 07 92 e-mail: karim.belmadi@talvor-consulting.example address: 17 Rue Marcel Danvin 92400 Courbevoie This visit will be used on the banking institutions and Talvor is a consulting firm. I do not want to have dark background.

Target Market(s)

banks

Contact Information for Business Card

Name : Karim Belmadi
Title : Director
mobile : +33(0)6 72 18 35 09
Phone : +33(0)4 58 61 07 92
e-mail: karim.belmadi@talvor-consulting.example
adresse : 17 Rue marcel Danvin 92400 Courbevoie

Requirements
Nice to have
• serious but not sad

```html
<!DOCTYPE html>
<html lang="en">
<head>
<meta charset="utf-8">
<title>Talvor business cards</title>
<link rel="stylesheet" href="https://fonts.googleapis.com/css2?family=Exo+2:wght@500;700&family=Lato:wght@400&display=swap">
<style>
  :root {
    --backdrop: #1b1b1b;
    --card: #f3f3f3;
    --ink: #4a4a4a;
    --ink-strong: #555555;
    --mark: #5e5e5e;
    --pattern-light: #f4f4f4;
    --pattern-mid: #dcdcdc;
  }
  html, body {
    margin: 0;
    padding: 0;
    width: 1200px;
    height: 900px;
    overflow: hidden;
    background: var(--backdrop);
  }
  .stage {
    position: relative;
    width: 1200px;
    height: 900px;
  }
  .card {
    position: absolute;
    top: 200px;
    width: 310px;
    height: 502px;
    background: var(--card);
    overflow: hidden;
  }
  .card-front {
    left: 291px;
    border-radius: 52px 0 52px 0;
  }
  .card-back {
    left: 627px;
    width: 309px;
    border-radius: 0 52px 0 52px;
  }
  .brand {
    position: absolute;
    display: flex;
    align-items: center;
    gap: 18px;
  }
  .brand-dot {
    border-radius: 50%;
    background: var(--mark);
  }
  .brand-name {
    font-family: "Exo 2", sans-serif;
    font-weight: 500;
    color: var(--mark);
    line-height: 1;
    letter-spacing: 0.5px;
  }
  .card-front .brand { left: 38px; top: 85px; }
  .card-front .brand-dot { width: 56px; height: 56px; }
  .card-front .brand-name { font-size: 46px; }

  .contact {
    position: absolute;
    left: 25px;
    top: 298px;
    font-family: "Lato", sans-serif;
    color: var(--ink);
    font-size: 14.5px;
    line-height: 19px;
  }
  .contact-name {
    font-family: "Exo 2", sans-serif;
    font-weight: 700;
    font-size: 18px;
    color: var(--ink-strong);
    letter-spacing: 0.4px;
    margin: 0;
    line-height: 22px;
  }
  .contact-title { margin: 0 0 15px; }
  .contact-lines { margin: 0 0 14px; }
  .contact-address { margin: 0; font-style: normal; }

  .back-pattern {
    position: absolute;
    inset: 0;
    background: linear-gradient(180deg, var(--pattern-mid) 0%, #e6e6e6 55%, var(--pattern-light) 100%);
  }
  .card-back .brand { left: 39px; top: 390px; }
  .card-back .brand-dot { width: 62px; height: 62px; }
  .card-back .brand-name { font-size: 46px; }
</style>
</head>
<body>
<main class="stage">
  <section class="card card-front">
    <div class="brand">
      <span class="brand-dot"></span>
      <span class="brand-name">Talvor</span>
    </div>
    <div class="contact">
      <p class="contact-name">KARIM BELMADI</p>
      <p class="contact-title">Director</p>
      <p class="contact-lines">+33(0)6 72 18 35 09<br>+33(0)4 58 61 07 92<br>karim.belmadi@talvor-consulting.example</p>
      <address class="contact-address">17 Rue Marcel Danvin<br>92150 Valmerine</address>
    </div>
  </section>
  <section class="card card-back">
    <div class="back-pattern" role="img" aria-label="Repeating pattern of the Talvor brand symbol in soft greys"></div>
    <div class="brand">
      <span class="brand-dot"></span>
      <span class="brand-name">Talvor</span>
    </div>
  </section>
</main>
</body>
</html>
```